Lydia Hartwell personal business/name cards and stationery brief

I am looking for a simple design on my personal business cards, that I may use for all my stationery. All my stationery would be cream or ivory textured card, or cream/ivory quality paper. I am director of my family company and also property developer. But am wishing to have basic business cards that I can use across both businesses. I do not wish to have a title, just my initials as a focal point.
Target Market(s)
These are my personal business cards and stationery. I am looking for an elegant, relatively understated design that exudes wealth. There is no target audience, other than clients or people I already do business with. However design must be stylish and timeless.
If I am handing out my business card to anyone I do not do business with, or they are not contracting to me or my company currently, then i would like the target audience to wish they were.
I am 54 yeas of age, and my business cards must denote respect and class.
Industry/Entity Type
Business
Contact Information for Business Card
LH
Lydia Hartwell
Justice of the Peace
Possible rear of card
Mobile number
Email
Font styles to use
Requirements
Must have
- LH to be somehow entwined as a logo on the front of the card above my name
- These cards must state that I am a Justice of the Peace
- Colours only ivory or cream card with texture, and gold elegant font.
- Must be able to be used on all my stationery products
- Must be elegant, timeless and not cluttered
- Below are just some design I like. There is something in each design I like.
Nice to have
- I would like my initials to be the centre piece of the card. Somehow entwined together elegantly in a logo of sorts that I can use across all my stationery. But if not my initials, then something that is different and stands out from the rest.
Should not have
- Not gawdy or young. No colour. Nothing outlandish.

```html
<!DOCTYPE html>
<html lang="en">
<head>
<meta charset="utf-8">
<title>Lydia Hartwell – Business Card</title>
<link href="https://fonts.googleapis.com/css2?family=Petit+Formal+Script&display=swap" rel="stylesheet">
<style>
  :root {
    --backdrop: #173c4a;
    --ivory: #fdf9d0;
    --gold-band: #fbe28c;
    --gold-text: #c98f2a;
    --gold-light: #f2d27a;
    --gold-deep: #d6a23c;
  }
  * { margin: 0; padding: 0; box-sizing: border-box; }
  html, body {
    width: 1200px;
    height: 1000px;
    overflow: hidden;
    background: var(--backdrop);
  }
  .card {
    position: absolute;
    left: 329px;
    width: 550px;
    height: 297px;
    background: var(--ivory);
  }
  .card--front { top: 147px; }
  .card--back { top: 538px; }
  .card__frame {
    position: absolute;
    left: 12px;
    top: 12px;
    right: 13px;
    bottom: 13px;
    border: 10px solid var(--gold-band);
  }
  .monogram-area {
    position: absolute;
    border-radius: 50%;
    background: radial-gradient(ellipse at center, var(--gold-deep) 0%, var(--gold-light) 55%, var(--ivory) 100%);
    opacity: 0.55;
  }
  .card--front .monogram-area {
    left: 191px;
    top: 61px;
    width: 170px;
    height: 142px;
  }
  .card--back .monogram-area {
    left: 384px;
    top: 147px;
    width: 117px;
    height: 102px;
  }
  .name-line {
    position: absolute;
    left: 0;
    right: 0;
    top: 224px;
    text-align: center;
    font-family: "Petit Formal Script", cursive;
    font-size: 18px;
    color: var(--gold-text);
    letter-spacing: 0.5px;
    word-spacing: 4px;
  }
  .contact {
    position: absolute;
    left: 54px;
    top: 48px;
    list-style: none;
    font-family: "Petit Formal Script", cursive;
    font-size: 16px;
    color: var(--gold-text);
    line-height: 33px;
    letter-spacing: 0.5px;
  }
</style>
</head>
<body>
  <section class="card card--front">
    <div class="card__frame"></div>
    <div class="monogram-area" role="img" aria-label="Entwined LH monogram in gold"></div>
    <p class="name-line">Lydia Hartwell / Justice of the Peace</p>
  </section>

  <section class="card card--back">
    <div class="card__frame"></div>
    <ul class="contact">
      <li class="contact__phone">+00 123456789</li>
      <li class="contact__email">lydia@hartwellmail.com</li>
    </ul>
    <div class="monogram-area" role="img" aria-label="Entwined LH monogram in gold"></div>
  </section>
</body>
</html>
```